Local fast-growing company in the service sector

We are looking for a modern business card design, which should also appear on our letterheads

Target Market(s)

Private and industrial sectors

Contact Information for Business Card

Vorname Name
Lindkofer Str. 18
71468 Kestenau
Tel.: 07163-418259-0
Name@kovaltec-pbz.de

Colors
9d9d9d
919191
aaaaaa

Requirements
Must have
• The logo (file) in silver

```html
<!DOCTYPE html>
<html lang="de">
<head>
<meta charset="utf-8">
<title>Kovaltec PBZ – Visitenkarte</title>
<link rel="stylesheet" href="https://fonts.googleapis.com/css2?family=Arimo:wght@400;700&display=swap">
<style>
  :root {
    --page-bg: #ececec;
    --card-left: #dcdcdc;
    --card-right: #9d9d9d;
    --divider-dark: #6f6f6f;
    --divider-light: #bdbdbd;
    --silver: #919191;
    --silver-light: #aaaaaa;
    --ink: #111111;
    --label: #e2e2e2;
    --icon-bg: #c7c7c7;
  }
  * { margin: 0; padding: 0; box-sizing: border-box; }
  html, body {
    width: 1200px;
    height: 970px;
    overflow: hidden;
    background: var(--page-bg);
    font-family: "Arimo", Arial, sans-serif;
  }
  .business-card {
    position: absolute;
    left: 100px;
    top: 184px;
    width: 1000px;
    height: 602px;
    border-radius: 20px;
    overflow: hidden;
    display: flex;
    box-shadow: 0 6px 24px rgba(0,0,0,0.12);
  }
  .card-brand {
    width: 514px;
    background: linear-gradient(135deg, #e6e6e6, var(--card-left));
    position: relative;
  }
  .card-divider { display: flex; width: 22px; }
  .card-divider .line-dark { width: 11px; background: var(--divider-dark); }
  .card-divider .line-light { width: 11px; background: var(--divider-light); }
  .card-contact {
    flex: 1;
    background: linear-gradient(160deg, #a6a6a6, var(--card-right) 60%, #8d8d8d);
    padding: 140px 0 0 20px;
    color: var(--ink);
  }
  .brand-lockup {
    position: absolute;
    left: 46px;
    top: 262px;
    display: flex;
    align-items: center;
    gap: 18px;
  }
  .brand-square {
    width: 84px;
    height: 84px;
    background: var(--silver);
    flex: none;
  }
  .brand-name {
    display: flex;
    flex-direction: column;
    color: var(--silver);
    font-weight: 700;
  }
  .brand-name .wordmark { font-size: 56px; line-height: 1; letter-spacing: 0.5px; }
  .brand-name .web { font-size: 27px; line-height: 1.1; }
  .person-name { font-size: 32px; font-weight: 700; line-height: 1.1; }
  .person-role { font-size: 19px; color: var(--label); margin-top: 4px; }
  .company-name {
    margin-top: 62px;
    font-size: 18px;
    color: var(--label);
    line-height: 1.15;
  }
  .address { font-size: 23px; line-height: 1.45; margin-top: 6px; }
  .contact-list { list-style: none; margin-top: 28px; }
  .contact-list li {
    display: flex;
    align-items: center;
    gap: 18px;
    font-size: 23px;
    height: 42px;
  }
  .contact-list .phone { letter-spacing: 2px; }
  .contact-icon {
    width: 30px;
    height: 30px;
    border-radius: 50%;
    background: var(--icon-bg);
    display: flex;
    align-items: center;
    justify-content: center;
    margin-left: 2px;
  }
</style>
</head>
<body>
  <article class="business-card">
    <section class="card-brand">
      <div class="brand-lockup">
        <div class="brand-square"></div>
        <div class="brand-name">
          <span class="wordmark">KOVALTEC</span>
          <span class="web">kovaltec-pbz.de</span>
        </div>
      </div>
    </section>
    <div class="card-divider"><span class="line-dark"></span><span class="line-light"></span></div>
    <section class="card-contact">
      <h1 class="person-name">JONAS WELLER</h1>
      <p class="person-role">CO-FOUNDER</p>
      <p class="company-name">KOVALTEC PBZ SERVICE GMBH<br>&amp; CO. KG</p>
      <p class="address">Lindkofer Str. 18 71468<br>Kestenau</p>
      <ul class="contact-list">
        <li>
          <span class="contact-icon">
            <svg width="16" height="16" viewBox="0 0 16 16" aria-hidden="true">
              <rect x="4" y="1" width="8" height="4" fill="#8a8a8a"/>
              <rect x="1" y="5" width="14" height="6" rx="1" fill="#8a8a8a"/>
              <rect x="4" y="9" width="8" height="6" fill="#8a8a8a" stroke="#c7c7c7" stroke-width="1"/>
            </svg>
          </span>
          <span class="phone">07163-418259-0</span>
        </li>
        <li>
          <span class="contact-icon">
            <svg width="16" height="16" viewBox="0 0 16 16" aria-hidden="true">
              <rect x="1" y="3" width="14" height="10" fill="#8a8a8a"/>
              <path d="M1 3 L8 9 L15 3" fill="none" stroke="#c7c7c7" stroke-width="1.2"/>
            </svg>
          </span>
          <span class="email">Name@kovaltec-pbz.de</span>
        </li>
      </ul>
    </section>
  </article>
</body>
</html>
```